Private Dining Restaurant Menu Design

Looking for help in designing a private dining room menu brochure - probably would need 4 panel layout to make all of the content fit, or a 5.5x8" booklet. Open to your ideas on layout/vessel - would want to post on website and be able to print to hand out to guests interested in booking our private dining room.

All content is in the attached "Private Dining Menu".

Would like to match existing dinner menu design - also attached.

Website is www.tallowfenkitchen.com

Requirements
Must have
• Easy to read format of a brochure of the private dining menu content - want to be able to hand out to interested guests and have it simple and easy to read/flip through.

```html
<!DOCTYPE html>
<html lang="en">
<head>
<meta charset="utf-8">
<title>Lunch Options</title>
<link href="https://fonts.googleapis.com/css2?family=Alegreya:wght@500;700&family=Roboto:ital,wght@0,400;0,500;0,700;1,400&display=swap" rel="stylesheet">
<style>
  :root {
    --navy-frame: #14275c;
    --navy-box: #1f3769;
    --navy-text: #1b2b5e;
    --cream: #ece8da;
    --sand: #ddd3bd;
    --white: #ffffff;
    --rust: #8a2a22;
    --ink: #222222;
  }
  * { margin: 0; padding: 0; box-sizing: border-box; }
  html, body { width: 825px; height: 1200px; overflow: hidden; }
  body { background: var(--navy-frame); font-family: "Roboto", Arial, sans-serif; }
  .menu { position: relative; width: 825px; height: 1200px; background: var(--navy-frame); }
  .sheet { position: absolute; left: 10px; top: 10px; width: 805px; height: 1180px; overflow: hidden; }
  .band { position: absolute; left: 0; width: 100%; }
  .band-hero { top: 0; height: 245px; background: linear-gradient(180deg, #d9d3c3 0%, #bdb39c 45%, #8c8169 80%, #74694f 100%); }
  .band-a { top: 245px; height: 376px; background: var(--cream); }
  .band-b { top: 621px; height: 277px; background: var(--sand); }
  .band-c { top: 898px; height: 282px; background: var(--white); }

  .title-box {
    position: absolute; left: 119px; top: 176px; width: 564px; height: 134px;
    background: var(--navy-box); border-radius: 12px; text-align: center; color: var(--white);
    box-shadow: 0 3px 8px rgba(0,0,0,0.25);
  }
  .title-box h1 { font-family: "Alegreya", Georgia, serif; font-weight: 500; font-size: 34px; letter-spacing: 0.5px; margin-top: 28px; }
  .title-box p { font-size: 15px; margin-top: 14px; color: #e4e6ee; }

  .option-title { position: absolute; font-family: "Alegreya", Georgia, serif; font-weight: 700; color: var(--rust); font-size: 24px; white-space: nowrap; }
  .option-title .per { font-size: 18px; font-weight: 500; }
  .option-note { position: absolute; font-style: italic; color: var(--rust); font-size: 13px; line-height: 15px; }

  .col { position: absolute; }
  .col h2 { font-size: 16px; font-weight: 500; color: var(--navy-text); margin-bottom: 14px; }
  .col li { list-style: none; font-size: 12.5px; color: var(--ink); line-height: 23px; }

  .dish-list { position: absolute; list-style: none; }
  .dish-list li { font-size: 13px; font-weight: 700; color: var(--navy-text); line-height: 23px; }
  .dish-list .detail { font-weight: 400; color: var(--ink); line-height: 16px; padding-left: 20px; text-align: justify; width: 297px; margin-bottom: 3px; }

  .photo-card { position: absolute; left: 445px; top: 674px; width: 320px; height: 477px; background: var(--navy-box); border-radius: 12px; box-shadow: 0 3px 8px rgba(0,0,0,0.3); }
  .photo { position: absolute; left: 9px; top: 32px; width: 304px; height: 305px; background: linear-gradient(160deg, #6e6253 0%, #a79a86 40%, #d8d2c4 70%, #5a4a3c 100%); }
  .card-trees { position: absolute; left: 0; bottom: 0; width: 100%; height: 120px; background: linear-gradient(180deg, rgba(70,95,150,0) 0%, rgba(70,95,150,0.45) 100%); border-radius: 0 0 12px 12px; }
</style>
</head>
<body>
<div class="menu">
  <div class="sheet">
    <div class="band band-hero" role="img" aria-label="Misty forest of pine trees with mountains and flying birds"></div>
    <div class="band band-a"></div>
    <div class="band band-b"></div>
    <div class="band band-c"></div>

    <header class="title-box">
      <h1>LUNCH OPTIONS</h1>
      <p>(an option must be chosen for groups of 15 or more, served before 3pm)</p>
    </header>

    <h2 class="option-title" style="left:52px; top:346px;">Option A - $10-$12<span class="per">/Person</span></h2>
    <p class="option-note" style="left:74px; top:388px;">Pick Two Lunch Menu – Soup/Salad ($10), Soup/Sandwich ($11), or Salad/Sandwich ($12)</p>

    <div class="col" style="left:73px; top:420px;">
      <h2>Sandwiches:</h2>
      <ul>
        <li>½ Turkey Club</li>
        <li>½ BLTA,</li>
        <li>BBQ Pork Sliders (2)</li>
        <li>Wood-Roasted Rotisserie Chicken Sliders (2)</li>
        <li>Walleye Tacos (2)</li>
        <li>Chicken Tacos (2)</li>
      </ul>
    </div>
    <div class="col" style="left:386px; top:420px;">
      <h2>Soups:</h2>
      <ul>
        <li>Chicken Wild Rice</li>
        <li>White Chicken Chili</li>
        <li>Soup of the Day</li>
      </ul>
    </div>
    <div class="col" style="left:589px; top:420px;">
      <h2>Salads:</h2>
      <ul>
        <li>Wedge</li>
        <li>House</li>
        <li>Caesar Salad</li>
      </ul>
    </div>

    <h2 class="option-title" style="left:50px; top:662px;">Option B - $13<span class="per">/Person</span></h2>
    <p class="option-note" style="left:73px; top:699px; width:320px;">Served with your choice of fries, cheesy hashbrowns, soup, or apple cabbage slaw</p>
    <ul class="dish-list" style="left:73px; top:742px;">
      <li>Applewood Bacon &amp; Fajita Chicken Salad</li>
      <li>Rotisserie Chicken Salad</li>
      <li>Brown Sugar Bacon and Smoked Cheddar Burger</li>
      <li>Pepperjack Turkey Melt</li>
      <li>Walleye Fish Tacos</li>
    </ul>

    <h2 class="option-title" style="left:50px; top:942px;">Option C - $13<span class="per">/Person Buffet Option</span></h2>
    <p class="option-note" style="left:73px; top:978px;">Food ready upon arrival, or at a set time of your choice</p>
    <ul class="dish-list" style="left:73px; top:1011px;">
      <li>Sandwich platter</li>
      <li class="detail">Assorted Rotisserie Turkey Club, Ham and Cheese, and Veggie Wrap</li>
      <li>Rotisserie Chicken Salad Bar</li>
      <li>Fresh Fruit Platter</li>
      <li>House-made Potato Chips</li>
    </ul>

    <aside class="photo-card">
      <div class="photo" role="img" aria-label="Private dining room with set tables, stone fireplace and pendant lights"></div>
      <div class="card-trees" role="img" aria-label="Faint pine tree silhouettes"></div>
    </aside>
  </div>
</div>
</body>
</html>
```